Harbor Healthcare Coming Soon Sign

I need a large (10 x5) road banner announcing the construction of our new medical practice at 5817 Marlow Creek Road in John's Island. The name of our practice is Harbor Healthcare and we thought it would be fund to nick name it the "Harbor Lookout". We'd like the tagline to read - "There's nothing healthy about driving an hour to see your doctor. So we're coming to you." Opening Late 2025 I have attached three logos as we have two other practices (Harbor Urgent and Harbor Aesthetics ) that should be present on the bottom of the sign but the main business is Harbor Healthcare. For more information on our look/feel visit our website www.wekeepitplain.example (which should be somewhere on the banner as well)
Updates

The signage needs to say Coming Late Fall 2025!

Target Market(s)

Drive By traffic must be made aware that we are coming soon

Industry/Entity Type

Healthcare

Requirements
Nice to have
• Western Theme

```html
<!DOCTYPE html>
<html lang="en">
<head>
<meta charset="utf-8">
<title>Harbor Healthcare – Coming Late Fall 2025</title>
<link rel="stylesheet" href="https://fonts.googleapis.com/css2?family=Heebo:wght@500;700;800&display=swap">
<style>
  :root {
    --page-bg: #e9edf1;
    --sign-white: #ffffff;
    --navy: #1d2a55;
    --sky-blue: #14b9ea;
    --deep-blue: #0a6ccb;
    --light-blue: #5aa9e2;
    --accent-pink: #e6195f;
    --accent-red: #e23a2c;
    --frame: #1d2a55;
  }
  * { box-sizing: border-box; margin: 0; padding: 0; }
  html, body {
    width: 1200px; height: 798px; overflow: hidden;
    background: var(--page-bg);
    font-family: "Heebo", Arial, sans-serif;
  }
  .canvas { position: relative; width: 1200px; height: 798px; }

  .sign {
    position: absolute; left: 40px; top: 119px;
    width: 1120px; height: 560px;
    background: var(--sign-white);
    border: 2px solid var(--frame);
  }
  .sign-inner {
    position: absolute; inset: 8px;
    border-top: 1px solid #c9ced8;
    overflow: hidden;
  }
  .footer-band { position: absolute; inset: 0; width: 100%; height: 100%; }

  .brand {
    position: absolute; left: 36px; top: 40px;
    display: flex; align-items: center; gap: 14px;
  }
  .brand-mark { width: 44px; height: 44px; border-radius: 50%; background: var(--light-blue); }
  .brand-name {
    font-weight: 800; font-size: 38px; letter-spacing: 2px;
    color: var(--navy); text-transform: uppercase; line-height: 1;
  }

  .opening-tag {
    position: absolute; right: 0; top: 31px;
    width: 432px; height: 55px;
    border-radius: 28px 0 0 28px;
    background: linear-gradient(90deg, var(--sky-blue), var(--deep-blue));
    display: flex; align-items: center; padding-left: 18px;
    box-shadow: 0 4px 8px rgba(0,0,0,0.15);
  }
  .opening-tag span {
    font-weight: 700; font-size: 30px; color: var(--navy); letter-spacing: 0.3px;
  }

  .tagline {
    position: absolute; left: 0; right: 0; top: 168px;
    text-align: center;
    font-weight: 700; font-size: 41px; line-height: 59px;
    color: var(--navy);
  }

  .sister-brands {
    position: absolute; left: 0; right: 0; top: 372px;
    display: flex; justify-content: center; gap: 46px;
  }
  .sister { display: flex; align-items: center; gap: 12px; }
  .sister-mark { width: 40px; height: 40px; }
  .sister-mark.aesthetics { border-radius: 50%; background: var(--accent-pink); }
  .sister-mark.urgent { background: var(--accent-red); border-radius: 4px; }
  .sister-name {
    font-weight: 700; font-size: 26px; letter-spacing: 2px;
    text-transform: uppercase; color: var(--navy);
  }

  .contact {
    position: absolute; bottom: 16px;
    display: flex; align-items: center; gap: 10px;
    font-weight: 700; font-size: 26px; color: var(--sign-white);
  }
  .contact.address { left: 28px; }
  .contact.website { right: 20px; }
  .contact svg { flex: none; }
</style>
</head>
<body>
<main class="canvas">
  <section class="sign" aria-label="Harbor Healthcare coming soon road banner">
    <div class="sign-inner">
      <svg class="footer-band" viewBox="0 0 1100 540" preserveAspectRatio="none" aria-hidden="true">
        <defs>
          <linearGradient id="bandGradient" x1="0" y1="0" x2="1" y2="0">
            <stop offset="0" stop-color="#14b9ea"/>
            <stop offset="1" stop-color="#0a6ccb"/>
          </linearGradient>
        </defs>
        <path d="M0 350 Q550 556 1100 350 L1100 540 L0 540 Z" fill="url(#bandGradient)"/>
        <path d="M0 362 Q550 564 1100 362 L1100 540 L0 540 Z" fill="#ffffff"/>
        <path d="M0 374 Q550 572 1100 374 L1100 540 L0 540 Z" fill="url(#bandGradient)"/>
      </svg>

      <div class="brand">
        <span class="brand-mark"></span>
        <span class="brand-name">Harbor Healthcare</span>
      </div>

      <div class="opening-tag"><span>Coming Late Fall 2025!</span></div>

      <h1 class="tagline">There's Nothing Healthy About Driving An<br>Hour To See Your Doctor. So We're Coming To You.</h1>

      <div class="sister-brands">
        <div class="sister">
          <span class="sister-mark aesthetics"></span>
          <span class="sister-name">Harbor Aesthetics</span>
        </div>
        <div class="sister">
          <span class="sister-mark urgent"></span>
          <span class="sister-name">Harbor Urgent</span>
        </div>
      </div>

      <div class="contact address">
        <svg width="26" height="36" viewBox="0 0 26 36" aria-hidden="true">
          <path d="M13 0C5.8 0 0 5.8 0 13c0 9.5 13 23 13 23s13-13.5 13-23C26 5.8 20.2 0 13 0z" fill="#fff"/>
          <circle cx="13" cy="13" r="5" fill="#14b9ea"/>
        </svg>
        <span>5817 Marlow Creek Road in John's Island</span>
      </div>

      <div class="contact website">
        <svg width="30" height="30" viewBox="0 0 30 30" aria-hidden="true" fill="none" stroke="#fff" stroke-width="1.8">
          <circle cx="15" cy="15" r="13"/>
          <ellipse cx="15" cy="15" rx="6" ry="13"/>
          <line x1="2" y1="15" x2="28" y2="15"/>
          <path d="M4 8h22M4 22h22"/>
        </svg>
        <span>www.wekeepitplain.example</span>
      </div>
    </div>
  </section>
</main>
</body>
</html>
```